Business Card Design Project

Hello- I am an interior stylist/product designer whose work is detail driven, very clean and transitional in style and I want my business card to reflect those qualities. I have a logo that I use on my website- my name and a hand drawn chandelier that I want incorporated into the design. However, "Design for the Home" needs to be changed to "Designs". I will be using cream colored stock and am thinking of gray text and logo. I need your help in pulling my card together since it will be the most used element and drive the design of the rest of my stationary suite.
Updates

Please note that I have changed my QR code from my cell # to my website. The new code will be downloaded now.

Reason: I want to thank everyone who has submitted designs- there are truly some very inspiring designs and I am very pleased. I want to make certain that I get this right and have an attractive and highly effective marketing tool when we are finished. With that said, I have run into a technical problem with one aspect of the card- a qr code for my website that was not part of the original brief. I will get that corrected today and post. Once I get that taken care of, I will post comments to all designs received do far. Thanks again for everyone's efforts, Risa

QR Code for the website is now uploaded. Thanks for your patience!

Target Market(s)

Upper middle class- mostly women

Industry/Entity Type

Business

Requirements
Must have
• Marisa Vantry Designs
"...to the last detail."
214-555-0148
marisavantry@plumwick.net
www.marisavantrydesigns-example.com
27083 Birchmont Court
Dallas, TX 75000
Nice to have
• Risa Vantry
Owner

```html
<!DOCTYPE html>
<html lang="en">
<head>
<meta charset="utf-8">
<title>Marisa Vantry Designs — Business Card</title>
<link href="https://fonts.googleapis.com/css2?family=Caveat+Brush&family=Kaushan+Script&display=swap" rel="stylesheet">
<style>
  :root {
    --paper: #f1ede2;
    --paper-shade: #e8e2d4;
    --ink: #7b5e58;
    --rule: #8a6e68;
  }
  html, body {
    margin: 0;
    padding: 0;
    width: 1200px;
    height: 667px;
    overflow: hidden;
    background: var(--paper);
  }
  .card {
    position: relative;
    width: 1200px;
    height: 667px;
    background: radial-gradient(ellipse at 40% 45%, var(--paper) 0%, var(--paper-shade) 100%);
    color: var(--ink);
    font-family: "Caveat Brush", cursive;
    overflow: hidden;
  }
  .chandelier-art {
    position: absolute;
    left: 94px;
    top: 70px;
    width: 447px;
    height: 518px;
    border-radius: 40px;
    background: radial-gradient(ellipse at 50% 45%, #c8b3ab 0%, #ddd0c6 55%, rgba(232,226,212,0) 80%);
  }
  .brand {
    position: absolute;
    left: 600px;
    width: 520px;
    top: 92px;
    text-align: center;
    white-space: nowrap;
  }
  .brand-name {
    margin: 0;
    font-family: "Kaushan Script", cursive;
    font-weight: 400;
    font-size: 70px;
    line-height: 1;
    letter-spacing: 1px;
    color: var(--ink);
  }
  .brand-tagline {
    margin: 8px 0 0;
    font-family: "Kaushan Script", cursive;
    font-size: 40px;
    line-height: 1;
    letter-spacing: 1.5px;
    color: var(--ink);
  }
  .brand-motto {
    margin: 10px 0 0;
    font-family: "Kaushan Script", cursive;
    font-size: 26px;
    line-height: 1;
    letter-spacing: 1px;
    color: var(--ink);
  }
  .divider {
    position: absolute;
    left: 640px;
    top: 285px;
    width: 445px;
    height: 3px;
    background: var(--rule);
  }
  .contact {
    position: absolute;
    left: 600px;
    width: 520px;
    top: 325px;
    margin: 0;
    padding: 0;
    list-style: none;
    text-align: center;
    font-size: 29px;
    line-height: 55px;
    letter-spacing: 0.5px;
    white-space: nowrap;
    color: var(--ink);
  }
  .contact li { margin: 0; }
  .contact .address { text-align: left; padding-left: 46px; }
  .contact .city { padding-left: 65px; }
</style>
</head>
<body>
  <main class="card">
    <div class="chandelier-art" role="img" aria-label="Hand-drawn three-arm chandelier with shaded lamps and scrolled ironwork"></div>

    <header class="brand">
      <h1 class="brand-name">Marisa Vantry</h1>
      <p class="brand-tagline">Designs</p>
      <p class="brand-motto">...to the last detail.</p>
    </header>

    <div class="divider"></div>

    <ul class="contact">
      <li class="phone">214-555-0148</li>
      <li class="email">marisavantry@plumwick.net</li>
      <li class="web">www.marisavantrydesigns-example.com</li>
      <li class="address">27083 Birchmont Court</li>
      <li class="address city">Dallas, TX 75000</li>
    </ul>
  </main>
</body>
</html>
```